Do an outer bag for a popular chocolate product

Wafa bloom is a small chocolate wafer, we have had a lot of demmand for the product to be packed in a bag to be bought in bulk. The bag will be 150 g and will contain about 13 small bars. The dimensions of bag flat are 240 mm long by 260mm wide. The bag should be modelled on the design of the chocolate bar attached. It should have a very similar look to the actual product and have a clear window in the centre of the pack through which the product is visible

Target Market(s)

Middle income consumers of chocoalate in Zimbabwe buying for family sharing, gifting or parties

Industry/Entity Type

Product

Requirements
Must have
• A window in the centre of the pack where the product is visible. The outer bag must be similar to the chocolate design as attached in the photo
Nice to have
• The use of half tones and swirls.

```html
<!DOCTYPE html>
<html lang="en">
<head>
<meta charset="utf-8">
<title>Wafa bloom – 150 g sharing bag</title>
<link href="https://fonts.googleapis.com/css2?family=Fredoka:wght@600;700&family=Cinzel:wght@600&display=swap" rel="stylesheet">
<style>
  :root {
    --backdrop: #1b78b4;
    --band-brown: #4a3a3a;
    --panel-red: #9e2a2f;
    --title-yellow: #f8c41c;
    --cream: #f6dfae;
    --choc-dark: #3b1f14;
    --choc-mid: #7a4630;
  }
  html, body {
    margin: 0;
    width: 1200px;
    height: 1200px;
    overflow: hidden;
    background: var(--backdrop);
  }
  .bag {
    position: absolute;
    left: 80px;
    top: 120px;
    width: 1040px;
    height: 960px;
    box-shadow: 0 18px 40px rgba(0,0,0,.35);
  }
  .bag-art { position: absolute; inset: 0; }
  .product-photo {
    position: absolute;
    border-radius: 10px;
    background: linear-gradient(135deg, var(--choc-mid), var(--choc-dark));
  }
  .product-photo--top { left: 100px; top: 150px; width: 320px; height: 210px; }
  .product-photo--bottom { left: 670px; top: 610px; width: 310px; height: 205px; }
  .brand-block {
    position: absolute;
    font-family: "Fredoka", sans-serif;
    color: var(--title-yellow);
    white-space: nowrap;
  }
  .brand-block p, .brand-block h1, .brand-block h2 { margin: 0; }
  .brand-block--main { left: 110px; top: 598px; }
  .brand-block--flipped { left: 530px; top: 178px; transform: rotate(180deg); }
  .maker-name {
    font-weight: 600;
    font-size: 30px;
    line-height: 34px;
    color: var(--cream);
    padding-left: 70px;
  }
  .product-name {
    font-weight: 700;
    font-size: 88px;
    line-height: 92px;
    text-shadow: 3px 4px 0 rgba(60,20,10,.45);
  }
  .product-descriptor {
    font-family: "Cinzel", serif;
    font-weight: 600;
    font-size: 26px;
    line-height: 32px;
    color: var(--cream);
    padding-left: 150px;
    letter-spacing: 1px;
  }
  .brand-block--flipped .maker-name { font-size: 20px; line-height: 24px; padding-left: 50px; }
  .brand-block--flipped .product-name { font-size: 68px; line-height: 72px; }
  .brand-block--flipped .product-descriptor { font-size: 20px; line-height: 26px; padding-left: 110px; }
</style>
</head>
<body>
  <main class="bag">
    <svg class="bag-art" viewBox="0 0 1040 960" width="1040" height="960" aria-hidden="true">
      <defs>
        <radialGradient id="panelGlow" cx="0.6" cy="0.55" r="0.7">
          <stop offset="0" stop-color="#b33a3d"/>
          <stop offset="1" stop-color="#8c2227"/>
        </radialGradient>
        <linearGradient id="ribbonTop" x1="0" x2="1">
          <stop offset="0" stop-color="#ffc21a"/>
          <stop offset="1" stop-color="#ff5a1e"/>
        </linearGradient>
        <linearGradient id="ribbonBottom" x1="0" x2="1">
          <stop offset="0" stop-color="#ff5a1e"/>
          <stop offset="1" stop-color="#ffc21a"/>
        </linearGradient>
        <mask id="windowCut">
          <rect width="1040" height="960" fill="#fff"/>
          <ellipse cx="610" cy="460" rx="260" ry="125" transform="rotate(-6 610 460)" fill="#000"/>
        </mask>
      </defs>
      <g mask="url(#windowCut)">
        <rect class="band-brown" width="1040" height="960" fill="#4a3a3a"/>
        <path class="panel-red" d="M0 170 C200 110 400 90 560 100 C760 115 920 150 1040 190 L1040 810 C940 850 800 890 620 885 C420 880 200 820 0 740 Z" fill="url(#panelGlow)"/>
      </g>
      <path class="ribbon-top" d="M0 170 C200 110 400 90 560 100 C760 115 920 150 1040 190" fill="none" stroke="url(#ribbonTop)" stroke-width="14"/>
      <path class="ribbon-bottom" d="M0 740 C200 820 420 880 620 885 C800 890 940 850 1040 810" fill="none" stroke="url(#ribbonBottom)" stroke-width="14"/>
      <ellipse class="window-rim" cx="610" cy="460" rx="260" ry="125" transform="rotate(-6 610 460)" fill="none" stroke="#ffa412" stroke-width="12"/>
    </svg>

    <div class="product-photo product-photo--top" role="img" aria-label="Photo of a chocolate-coated wafer bar with a cut piece showing wafer layers"></div>
    <div class="product-photo product-photo--bottom" role="img" aria-label="Photo of a chocolate-coated wafer bar with a cut piece showing wafer layers"></div>

    <div class="brand-block brand-block--flipped">
      <p class="maker-name">Kudya Snacks</p>
      <h2 class="product-name">Wafa bloom</h2>
      <p class="product-descriptor">Choc Coated Wafer</p>
    </div>

    <div class="brand-block brand-block--main">
      <p class="maker-name">Kudya Snacks</p>
      <h1 class="product-name">Wafa bloom</h1>
      <p class="product-descriptor">Choc Coated Wafer</p>
    </div>
  </main>
</body>
</html>
```